Ridgeway Framers Business Card

I'm looking for a business card design for a start-up Handyman/Construction Company. The organization will double as a ministry to the homeless, hoping to create job opportunity and training to the homeless, providing a pathway back to being "homed". I'm looking for a simple to "seeming" simple design. Open to all thoughts.

Industry/Entity Type

Ministry

Requirements
Must have
• Logo (Attached), Name, Phone, Email and Address. Note - "*Registered and Insured".

```html
<!DOCTYPE html>
<html lang="en">
<head>
<meta charset="utf-8">
<title>Ridgeway Framers Business Card</title>
<link rel="stylesheet" href="https://fonts.googleapis.com/css2?family=Arimo:wght@400;700&display=swap">
<style>
  :root {
    --page-bg: #e9e7e4;
    --card-white: #f7f7f7;
    --navy-deep: #0f3466;
    --navy-mid: #2b5082;
    --navy-light: #5a7aa6;
    --brand-ink: #34507d;
    --text-light: #ffffff;
  }
  * { margin: 0; padding: 0; box-sizing: border-box; }
  html, body {
    width: 1200px;
    height: 1000px;
    overflow: hidden;
    background: var(--page-bg);
    font-family: "Arimo", Arial, sans-serif;
  }
  .stage {
    width: 1200px;
    height: 1000px;
    display: flex;
    align-items: center;
    justify-content: center;
  }
  .business-card {
    position: relative;
    width: 900px;
    height: 510px;
    border-radius: 34px;
    overflow: hidden;
    background: var(--card-white);
    box-shadow: 0 10px 30px rgba(0, 0, 0, 0.18);
  }
  .card-top {
    position: absolute;
    inset: 0 0 auto 0;
    height: 205px;
    background: var(--card-white);
  }
  .card-band {
    position: absolute;
    inset: 205px 0 0 0;
    background:
      radial-gradient(ellipse 420px 260px at 50% 0%, var(--navy-light) 0%, var(--navy-mid) 45%, transparent 100%),
      linear-gradient(90deg, var(--navy-mid) 0%, var(--navy-deep) 100%);
  }
  .brand-name {
    position: absolute;
    left: 50%;
    top: 136px;
    transform: translateX(-50%);
    display: flex;
    align-items: center;
    gap: 14px;
    font-size: 52px;
    font-weight: 700;
    color: var(--brand-ink);
    white-space: nowrap;
    letter-spacing: 0.5px;
  }
  .brand-mark {
    width: 20px;
    height: 20px;
    border-radius: 50%;
    background: var(--brand-ink);
  }
  .person-name {
    position: absolute;
    left: 70px;
    top: 258px;
    font-size: 32px;
    font-weight: 700;
    color: var(--text-light);
  }
  .card-note {
    position: absolute;
    left: 44px;
    top: 336px;
    font-size: 15px;
    color: var(--text-light);
  }
  .contact-list {
    position: absolute;
    left: 560px;
    top: 366px;
    list-style: none;
    color: var(--text-light);
    font-size: 18px;
  }
  .contact-list li {
    display: flex;
    align-items: center;
    gap: 10px;
    height: 32px;
  }
  .contact-icon {
    width: 16px;
    height: 16px;
    flex: none;
    fill: var(--text-light);
  }
</style>
</head>
<body>
<main class="stage">
  <section class="business-card">
    <div class="card-top"></div>
    <div class="card-band"></div>

    <div class="brand-name"><span class="brand-mark"></span>Ridgeway Framers</div>

    <h1 class="person-name">Person Name</h1>
    <p class="card-note">Note: "Registered and Insured"</p>

    <ul class="contact-list">
      <li>
        <svg class="contact-icon" viewBox="0 0 16 16" aria-hidden="true"><path d="M8 1 L15 7.5 H13 V15 H9.5 V10.5 H6.5 V15 H3 V7.5 H1 Z"/></svg>
        Address address address address
      </li>
      <li>
        <svg class="contact-icon" viewBox="0 0 16 16" aria-hidden="true"><path d="M3.5 1.5 L6 1 L7.5 4.5 L5.8 5.8 C6.6 7.7 8.3 9.4 10.2 10.2 L11.5 8.5 L15 10 L14.5 12.5 C14.2 14 12.8 15 11.3 14.7 C6.4 13.7 2.3 9.6 1.3 4.7 C1 3.2 2 1.8 3.5 1.5 Z"/></svg>
        012345678910
      </li>
      <li>
        <svg class="contact-icon" viewBox="0 0 16 16" aria-hidden="true"><path d="M8 1a7 7 0 1 0 3.5 13.1l-.6-1.2A5.7 5.7 0 1 1 13.7 8v.8c0 .9-.6 1.5-1.3 1.5s-1.2-.6-1.2-1.5V4.6H10v.6A3.2 3.2 0 1 0 10.3 10.6 2.5 2.5 0 0 0 12.4 11.6C13.9 11.6 15 10.4 15 8.8V8A7 7 0 0 0 8 1Zm0 9a2 2 0 1 1 0-4 2 2 0 0 1 0 4Z"/></svg>
        xxxxxxxxxx@xxxxx.xxx
      </li>
    </ul>
  </section>
</main>
</body>
</html>
```